Self Defence Seminar Flyer

Need a flyer that will sell a seminar that will teach self defence techniques to customers. Needs to have a good image that will remind people about the dangerous world. The seminar is for men and women.

Needs to look professional.

I have attached the previous flyer we used. needs same information except without the same date and time for seminar.

Target Market(s)

Male and Females interested in learning how to defend themselves or family

Industry/Entity Type

Defence

Requirements
Must have
• A Image that reminds people of a dangerous situation

```html
<!DOCTYPE html>
<html lang="en">
<head>
<meta charset="utf-8">
<title>Self Defence Seminar</title>
<link rel="stylesheet" href="https://fonts.googleapis.com/css2?family=Alfa+Slab+One&family=Lato:wght@400;700&display=swap">
<style>
  :root {
    --wood-dark: #24170f;
    --wood-mid: #4a3222;
    --wood-light: #5e4130;
    --plank-line: rgba(10, 5, 2, 0.55);
    --title-grey: #dadada;
    --panel-top: #9c9c9c;
    --panel-bottom: #c9c9c9;
    --body-ink: #111111;
    --info-grey: #a8a8a8;
    --price-grey: #c4c4c4;
    --url-blue: #9fd3df;
    --badge-red: #c8102e;
    --badge-dark: #1e1c20;
    --badge-light: #eeeeee;
    --hero-warm: #8a6a45;
    --hero-mid: #4e3a2c;
    --hero-dark: #1c1713;
  }
  * { margin: 0; padding: 0; box-sizing: border-box; }
  html, body { width: 900px; height: 1200px; overflow: hidden; background: var(--wood-dark); }
  .flyer {
    position: relative;
    width: 900px;
    height: 1200px;
    overflow: hidden;
    font-family: "Lato", sans-serif;
    background:
      repeating-linear-gradient(90deg, transparent 0 128px, var(--plank-line) 128px 131px, transparent 131px 224px),
      linear-gradient(90deg, var(--wood-dark) 0%, var(--wood-mid) 30%, var(--wood-light) 55%, var(--wood-mid) 80%, var(--wood-dark) 100%);
  }
  .flyer-title {
    position: absolute;
    top: 18px;
    left: 0;
    width: 900px;
    text-align: center;
    white-space: nowrap;
    font-family: "Alfa Slab One", serif;
    font-weight: 400;
    font-size: 59px;
    line-height: 50px;
    letter-spacing: 0.5px;
    color: var(--title-grey);
    text-shadow: 2px 3px 4px rgba(0,0,0,0.6);
    transform: scaleY(1.3);
    transform-origin: top center;
  }
  .hero-image {
    position: absolute;
    top: 105px;
    left: 0;
    width: 416px;
    height: 590px;
    background:
      radial-gradient(ellipse 45% 40% at 62% 52%, rgba(150,110,85,0.55) 0%, transparent 100%),
      linear-gradient(90deg, var(--hero-warm) 0%, var(--hero-mid) 35%, #3a2e28 70%, var(--hero-dark) 100%);
  }
  .info-panel {
    position: absolute;
    top: 105px;
    left: 416px;
    width: 484px;
    height: 590px;
    background: linear-gradient(180deg, var(--panel-top) 0%, var(--panel-bottom) 100%);
    padding: 26px 0 0 14px;
  }
  .info-list { list-style: none; width: 462px; }
  .info-list li {
    position: relative;
    padding-left: 15px;
    margin-bottom: 30px;
    font-weight: 700;
    font-size: 20.5px;
    line-height: 26px;
    color: var(--body-ink);
  }
  .info-list li::before {
    content: "•";
    position: absolute;
    left: 0;
  }
  .partner {
    position: absolute;
    top: 678px;
    display: flex;
    align-items: center;
    justify-content: center;
    text-align: center;
    padding: 10px;
    font-weight: 700;
    font-size: 20px;
    line-height: 24px;
  }
  .partner-ironline { left: 112px; width: 146px; height: 146px; background: var(--badge-red); color: #ffffff; }
  .partner-team { left: 338px; width: 219px; height: 146px; background: var(--badge-light); color: var(--badge-dark); }
  .partner-academy { left: 665px; width: 145px; height: 146px; background: var(--badge-dark); color: #ffffff; }
  .venue {
    position: absolute;
    top: 934px;
    left: 38px;
    font-weight: 700;
    font-size: 29px;
    line-height: 35px;
    color: var(--info-grey);
  }
  .price {
    position: absolute;
    top: 926px;
    left: 645px;
    font-weight: 700;
    font-size: 76px;
    line-height: 84px;
    color: var(--price-grey);
  }
  .price-currency { font-size: 88px; }
  .price-underline { position: absolute; top: 1010px; left: 642px; }
  .signup {
    position: absolute;
    top: 1080px;
    left: 0;
    width: 900px;
    text-align: center;
    font-weight: 700;
    font-size: 35px;
    color: var(--info-grey);
  }
  .website {
    position: absolute;
    top: 1118px;
    left: 0;
    width: 900px;
    text-align: center;
    font-weight: 700;
    font-size: 52px;
    letter-spacing: 1px;
    color: var(--url-blue);
  }
</style>
</head>
<body>
<main class="flyer">
  <h1 class="flyer-title">SELF DEFENCE SEMINAR</h1>

  <div class="hero-image" role="img" aria-label="Photograph placeholder: an attacker restraining a woman from behind, covering her mouth and holding a handgun, in a dim hallway"></div>

  <section class="info-panel">
    <ul class="info-list">
      <li>Being a victim is a topic that people would like to avoid. Unfortunately, we live in an increasingly dangerous society for men and women alike. Learning to defend yourself is an important like skill.</li>
      <li>Spend 2 hours with us learning some simple and effective Self Defence tactics that one-day may be needed to defend yourself or loved ones.</li>
      <li>Our aim is to teach you effective and efficient techniques and tactics to be able to defend yourself in a range of situations.</li>
      <li>Learn the same techniques and tactics that we have taught to individuals in Law enforcement Security and Military.</li>
    </ul>
  </section>

  <div class="partner partner-ironline">Ironline Fight Club</div>
  <div class="partner partner-team">Team NCA</div>
  <div class="partner partner-academy">Northgate Combat Academy</div>

  <p class="venue">Location: Northgate Combat Academy Gym<br>(12 Ridgeway Rd. Eastfield NSW)</p>

  <p class="price"><span class="price-currency">$</span>60.00</p>
  <svg class="price-underline" width="240" height="16" viewBox="0 0 240 16" aria-hidden="true">
    <path d="M4 9 Q120 2 236 9 Q120 13 4 9 Z" fill="#e6e6e6"/>
  </svg>

  <p class="signup">Sign up today by contacting us through our website</p>
  <p class="website">www.northgatecombat.com</p>
</main>
</body>
</html>
```